Buch-/E-Book-Cover Existenzgründer und Gründungsinteressierte
Zielgruppe
Es geht um eine Buchcover mit dem Titel 'Wolkenhafen erkunden'; Zielgruppe sind Existenzgründer und Gründungsinteressierte
Aufgabenstellung
Das Buchcover sollte modern und frisch gestaltet werden, eine grobe Skizze ist beigefügt, unten rechts soll das Verlagslogo (klein) platziert werden
Haupttext „Wolkenhafen erkunden“ soll auffallend, vielleicht als Wortmarke, gestaltet werden – er sollte einen Wiedererkennungswert haben
Auf der Frontseite des Covers sollten auch die Schlüsselwörter zu den Hauptkapiteln integriert werden (siehe Idee Skizze), damit der Leser auf den 1. Blick einen Eindruck über die Inhalte des Ratgebers gewinnt
Format: Das Taschenbuch soll im Hochformat (13,97 cm x 21,59 cm, Bindung links, Veltrano Quill Print Service) erscheinen und das Buch hat ca. 190 Seiten. Das Cover soll ein Softcover (235g Chromokarton), 4/4 farbig sein.

```html
<!DOCTYPE html>
<html lang="de">
<head>
<meta charset="utf-8">
<title>Wolkenhafen erkunden – Buchcover</title>
<link href="https://fonts.googleapis.com/css2?family=Anton&family=Oswald:wght@500;600&display=swap" rel="stylesheet">
<style>
  :root {
    --title-yellow: #f6c51b;
    --band-red: #e43c2c;
    --paper: #ffffff;
    --art-light: #e4eef3;
    --art-mid: #bcd6e0;
    --art-teal: #2f7f9c;
    --art-navy: #1d3a6b;
    --text-white: #ffffff;
  }
  html, body {
    margin: 0;
    padding: 0;
    overflow: hidden;
    background: var(--paper);
  }
  .cover {
    position: relative;
    width: 776px;
    height: 1200px;
    overflow: hidden;
    background: var(--paper);
  }
  .title {
    position: absolute;
    left: 34px;
    top: 22px;
    margin: 0;
    font-family: "Anton", "Oswald", sans-serif;
    font-weight: 400;
    color: var(--title-yellow);
    font-size: 128px;
    line-height: 130px;
    letter-spacing: 6px;
    text-transform: uppercase;
  }
  .title span { display: block; white-space: nowrap; }
  .subtitle-band {
    position: absolute;
    left: 31px;
    top: 428px;
    width: 703px;
    height: 52px;
    background: var(--band-red);
    color: var(--text-white);
    font-family: "Oswald", sans-serif;
    font-weight: 500;
    font-size: 33px;
    line-height: 52px;
    text-align: center;
    letter-spacing: 0.5px;
    text-transform: uppercase;
  }
  .illustration {
    position: absolute;
    left: 0;
    top: 492px;
    width: 776px;
    height: 708px;
    background: linear-gradient(90deg,
      var(--art-light) 0%,
      var(--art-mid) 22%,
      var(--art-teal) 36%,
      var(--art-navy) 50%,
      var(--art-teal) 64%,
      var(--art-mid) 78%,
      var(--art-light) 100%);
  }
  .chapters {
    position: absolute;
    left: 0;
    top: 690px;
    margin: 0;
    padding: 0;
    list-style: none;
  }
  .chapters li {
    height: 32px;
    margin-bottom: 15px;
    padding: 0 10px 0 6px;
    background: var(--band-red);
    color: var(--text-white);
    font-family: "Oswald", sans-serif;
    font-weight: 500;
    font-size: 26px;
    line-height: 32px;
    text-transform: uppercase;
    white-space: nowrap;
    width: fit-content;
  }
  .chapters li::before { content: "· "; }
  .author {
    position: absolute;
    left: 28px;
    top: 1134px;
    margin: 0;
    padding: 2px 8px;
    background: var(--paper);
    font-family: "Oswald", sans-serif;
    font-weight: 500;
    font-size: 24px;
    color: var(--band-red);
    text-transform: uppercase;
  }
  .publisher {
    position: absolute;
    left: 646px;
    top: 1052px;
    width: 96px;
    height: 118px;
    background: var(--paper);
    display: flex;
    flex-direction: column;
    align-items: center;
    justify-content: center;
    gap: 8px;
  }
  .publisher-square {
    width: 26px;
    height: 26px;
    background: var(--title-yellow);
  }
  .publisher-name {
    font-family: "Oswald", sans-serif;
    font-weight: 600;
    font-size: 20px;
    line-height: 22px;
    color: var(--band-red);
    text-align: center;
    text-transform: uppercase;
  }
</style>
</head>
<body>
  <main class="cover">
    <div class="illustration" role="img" aria-label="Illustration: Geschäftsmann im blauen Anzug mit gelber Krawatte, umgeben von Händen mit Pokal, Bankgebäude, Zahnrad, Diagramm und Münzen vor Zahnrädern und Blättern"></div>

    <h1 class="title">
      <span>Wolken-</span>
      <span>hafen</span>
      <span>erkunden</span>
    </h1>

    <div class="subtitle-band">Existenzgründung für Kleinunternehmen</div>

    <ul class="chapters">
      <li>Behördengänge</li>
      <li>Rechtsform</li>
      <li>(Digitale) Büroorgisation</li>
      <li>Buchhaltung und Steuern</li>
      <li>Finanzierung und Fördermittel</li>
      <li>Businessplan</li>
      <li>Versicherungen</li>
      <li>Bonus: Online-Trainings und Vorlagen</li>
    </ul>

    <p class="author">von Jonas Brettner</p>

    <div class="publisher">
      <span class="publisher-square"></span>
      <span class="publisher-name">Kassenklar<br>Verlag</span>
    </div>
  </main>
</body>
</html>
```